Digital Marketing Agency Needs a Pagecraft Web Design

We need a web design for a new company based in Evergreen, Colorado (the greater Denver Metro area) called "Copper Wayfarer". We are a full service Digital Marketing Agency that offers and provides the following services to clients: Website Design, Search Engine Optimization, Plexo Local Listing, Local Online Directories, Reputation Marketing, Social Media Marketing, Video Marketing, Pay Per Click. Our slogan is "Digital Marketing, Elevated!" We want a PageCraft web design that has a very modern look. We would like to see designs use the following colors (included color code):

light blue (#0cb9ea)
orange (#f47528)
white (#ffffff)
black (#000000).

These colors coincide with the colors of our logo (attached). We prefer a flat design but would like some elements of depth. We need a header that includes a logo (attached), name/address/phone number of our company, a contact call-to-action button (these need to be very easy to locate on the page), menu bar, and banner (very flexible to set up of banner).. The footer needs to include logo, NAP, Footer Menu, Section for blogs (includes title of blog that links to post), & copyright. We also need a way to prominently display and link our key featured services (Website Design, Search Engine Optimization, Plexo Local Listing, Local Online Directories, Reputation Marketing, Social Media Marketing, Video Marketing, Pay Per Click).

Here are three websites that we really like and would like to see certain elements incorporated:

1. http://quillstonemedia.example/ (like how the services were laid out on the home page for services -- "Features" section... want to follow this same type of idea, just in our own way).
2. http://tavenmark.example/ (love the modern, visual aspect of this site and how professionally clean it is.... very easy to understand and navigate through).
3. http://norvacreative.example/ (like how this site incorporates interactive features that engage people while visiting the site).

The overall goal of the site is to effectively emphasize the services we provide (see above), who we are, and how to contact us for services.

** Any stock photos used HAVE TO BE TAKEN from Lumafold Pictures (http://www.lumafoldpics.example/). And if watermarked, please provide the image code for each image used.

Target Market(s)

Lawyers, Insurance agents, Real Estate, Restaurant Owners, Doctors and all other medical providers.

Industry/Entity Type

Internet

Number of Pages Required

1 page

Font styles to use
Serif

Colors
33a6d7
ffffff
000000
f37122

Requirements
Must have
• 1. Header w/ Logo, Name/Address/Phone Number of our business, a call-to-action button to "Contact us":
• Copper Wayfarer – Digital Marketing
• 41872 Cobblewick Drive
• Larkmoor Valley 00142
• 555-547-9183
• 2. Navigation Menu
• 3. Some type of banner
• 4. Featured Services section (with a short blurb about each)
• 5. Contact Form (somewhere above the fold)
• 6. Need at least 2-3 paragraphs of text (use dummy text) somewhere on the page (either in full or in sections)....
• 7. Footer that includes logo, NAP (see above), Menu Links, Links for services (see above), Blog Section, Social Media icons (Chatterly, Peepline, Plexo+, and ReelHub) & a copyright.
Nice to have
• Here are three websites that we really like and would be nice to see elements of incorporated:
• 1. http://quillstonemedia.example/ (like how the services were laid out on the home page -- "Features" section... want to follow this same type of idea, just in our own way).
• 2. http://tavenmark.example/ (love the modern, visual aspect of this site and how professionally clean it is.... very easy to understand and navigate through).
• 3. http://norvacreative.example/ (like how this site incorporates interactive features that engage people that visit the site).
Should not have
• Pretty flexible... We just need to make sure it's a Pagecraft web design.

```html
<!DOCTYPE html>
<html lang="en">
<head>
<meta charset="utf-8">
<title>Copper Wayfarer – Digital Marketing</title>
<link rel="stylesheet" href="https://fonts.googleapis.com/css2?family=Raleway:wght@300;400;600;700&family=Open+Sans:wght@400;600&display=swap">
<style>
:root{
  --orange:#f47528;
  --blue:#0cb9ea;
  --blue-deep:#33a6d7;
  --ink:#222222;
  --text:#555555;
  --white:#ffffff;
  --footer:#2b2b2b;
  --footer-bottom:#1f1f1f;
}
*{box-sizing:border-box;margin:0;padding:0}
html,body{width:1200px;height:2228px;overflow:hidden;background:var(--white)}
body{font-family:"Open Sans",Arial,sans-serif;color:var(--text);position:relative}
.page{position:relative;width:1200px;height:2228px}

.info-bar{position:absolute;top:0;left:0;width:1200px;height:28px;background:var(--orange);color:var(--white);font-size:11px;line-height:28px}
.info-bar .nap{position:absolute;left:0;width:1200px;text-align:center}
.info-bar .phone{position:absolute;right:150px}

.contact-bar{position:absolute;top:28px;left:0;width:1200px;height:68px;background:var(--blue)}
.contact-bar .avatar{position:absolute;left:232px;top:10px;width:48px;height:48px;border-radius:50%;background:#dff5fc}
.contact-bar label{position:absolute;top:22px;color:var(--white);font-family:"Raleway",sans-serif;font-size:18px}
.contact-bar .field{position:absolute;top:18px;height:28px;background:var(--white);border-radius:2px}
.contact-bar .send{position:absolute;left:860px;top:18px;width:96px;height:28px;background:var(--orange);color:var(--white);font-size:12px;line-height:28px;text-align:center;border-radius:2px}

.nav-bar{position:absolute;top:96px;left:0;width:1200px;height:132px;background:var(--white)}
.brand{position:absolute;left:184px;top:52px;display:flex;align-items:center;gap:8px;font-family:"Raleway",sans-serif;font-weight:700;font-size:18px;color:var(--orange)}
.brand .dot{width:14px;height:14px;border-radius:50%;background:var(--blue)}
.menu{position:absolute;left:448px;top:64px;display:flex;gap:6px;list-style:none;font-size:13px}
.menu li{padding:6px 18px;color:#666}
.menu li.active{background:var(--blue);color:var(--white)}

.hero{position:absolute;top:228px;left:0;width:1200px;height:472px;background:linear-gradient(120deg,#8fd3ee 0%,#3db7e5 45%,#6cc7ea 100%)}
.hero h1{position:absolute;top:158px;width:1200px;text-align:center;font-family:"Raleway",sans-serif;font-weight:400;font-size:40px;color:var(--white)}
.hero p{position:absolute;top:222px;left:380px;width:440px;text-align:center;font-size:13px;line-height:20px;color:var(--white)}
.hero .more{position:absolute;top:318px;left:560px;width:80px;height:26px;background:var(--orange);color:var(--white);font-size:11px;line-height:26px;text-align:center}

.intro{position:absolute;top:700px;left:0;width:1200px;height:320px}
.intro h2{position:absolute;top:58px;width:1200px;text-align:center;font-family:"Raleway",sans-serif;font-weight:400;font-size:30px;color:var(--ink)}
.intro .rule{position:absolute;top:112px;left:350px;width:500px;height:1px;background:#999}
.intro p{position:absolute;top:130px;left:230px;width:740px;text-align:center;font-size:17px;line-height:27px;color:#555}

.services{position:absolute;top:1020px;left:0;width:1200px;height:360px;background:linear-gradient(180deg,#6b8aa3 0%,#4f6f8b 45%,#8aa3b6 60%,#2f4d66 100%)}
.services h2{position:absolute;top:34px;width:1200px;text-align:center;font-family:"Raleway",sans-serif;font-weight:400;font-size:28px;color:var(--white)}
.service{position:absolute;top:110px;width:200px;text-align:center;color:var(--white)}
.service .icon{width:64px;height:64px;margin:0 auto;border-radius:50%;background:var(--white)}
.service h3{margin-top:8px;font-weight:400;font-size:17px}
.service p{margin-top:6px;font-size:11px;line-height:15px}
.arrow{position:absolute;top:140px}

.reviews{position:absolute;top:1380px;left:0;width:1200px;height:460px}
.reviews h2{position:absolute;top:62px;width:1200px;text-align:center;font-family:"Raleway",sans-serif;font-weight:400;font-size:30px;color:var(--ink)}
.reviews h2 strong{color:var(--blue);font-weight:700}
.stars{position:absolute;top:128px;left:516px;display:flex;gap:8px}
.quote-mark{position:absolute;top:178px;left:408px;font-family:"Raleway",sans-serif;font-size:60px;line-height:60px;color:var(--blue)}
.reviews blockquote{position:absolute;top:194px;left:440px;width:320px;text-align:center;font-size:15px;line-height:22px;color:#555}
.reviews cite{position:absolute;top:296px;width:1200px;text-align:center;font-style:normal;font-size:11px;color:var(--blue)}
.dots{position:absolute;top:320px;left:580px;display:flex;gap:6px}
.dots span{width:7px;height:7px;border-radius:50%;background:#cfcfcf}
.dots span.on{background:var(--orange)}

.footer-brand{position:absolute;top:1866px;left:0;width:1200px;display:flex;justify-content:center;align-items:center;gap:8px;font-family:"Raleway",sans-serif;font-weight:700;font-size:18px;color:var(--orange)}
.footer-brand .dot{width:14px;height:14px;border-radius:50%;background:var(--blue)}

.footer{position:absolute;top:1916px;left:0;width:1200px;height:312px;background:var(--footer);color:#bbb}
.footer h4{font-family:"Raleway",sans-serif;font-weight:400;font-size:20px;color:var(--white)}
.footer h4 span{color:var(--orange)}
.footer .col{position:absolute;top:32px}
.footer .about p{margin-top:14px;width:200px;font-size:11px;line-height:17px}
.footer .about p em{font-style:normal;color:var(--orange)}
.footer ul{list-style:none;margin-top:14px;font-size:11px;line-height:17px}
.socials{display:flex;gap:12px;margin-top:16px}
.socials span{width:30px;height:30px;border-radius:3px}
.footer .bottom{position:absolute;left:0;bottom:0;width:1200px;height:38px;background:var(--footer-bottom);font-size:11px;line-height:38px;color:#999}
.footer .bottom .copy{position:absolute;left:120px}
.footer .bottom .legal{position:absolute;left:960px}
</style>
</head>
<body>
<div class="page">

  <div class="info-bar">
    <span class="nap">Copper Wayfarer - Digital Marketing 41872 Cobblewick Drive - Larkmoor Valley 00142 - 555-547-9183</span>
    <span class="phone">555-547-9183</span>
  </div>

  <div class="contact-bar">
    <div class="avatar"></div>
    <label style="left:360px">Name</label>
    <div class="field" style="left:418px;width:160px"></div>
    <label style="left:604px">E-mail</label>
    <div class="field" style="left:668px;width:176px"></div>
    <div class="send">Send</div>
  </div>

  <header class="nav-bar">
    <div class="brand"><span class="dot"></span>Copper Wayfarer</div>
    <ul class="menu">
      <li class="active">Home</li>
      <li>About Us</li>
      <li>Service</li>
      <li>Portfolio</li>
      <li>Client reviews</li>
      <li>Contact Us</li>
    </ul>
  </header>

  <section class="hero" role="img" aria-label="Photo of a person working on a laptop with a light blue overlay">
    <h1>YOUR HEADING</h1>
    <p>Lorem ipsum dolor sit amet, consectetur adipiscing elit, sed do eiusmod tempor incididunt ut labore et dolore magna aliqua. Ut enim ad minim veniam, quis nostrud exercitation ullamco laboris nisi ut aliquip ex ea commodo consequat. Duis aute irure dolor.</p>
    <div class="more">More</div>
  </section>

  <section class="intro">
    <h2>YOUR SUBTITLE GOES HERE</h2>
    <div class="rule"></div>
    <p>Lorem ipsum dolor sit amet, consectetur adipiscing elit, sed do eiusmod tempor incididunt ut labore et dolore magna aliqua. Ut enim ad minim veniam, quis nostrud exercitation ullamco laboris nisi ut aliquip ex ea commodo consequat. Duis aute irure dolor in reprehenderit in voluptate velit esse cillum dolore eu fugiat nulla pariatur.</p>
  </section>

  <section class="services" role="img" aria-label="Mountain lake landscape at dusk in blue tones">
    <h2>SERVICES</h2>
    <div class="service" style="left:188px">
      <div class="icon"></div>
      <h3>Internet</h3>
      <p>Lorem ipsum dolor sit amet, consectetur adipiscing elit, sed do eiusmod tempor incididunt ut labore.</p>
    </div>
    <svg class="arrow" style="left:412px" width="96" height="40" viewBox="0 0 96 40"><path d="M4 26 Q48 4 84 20" fill="none" stroke="#fff" stroke-width="5" stroke-linecap="round"/><path d="M72 8 L88 21 L70 30" fill="none" stroke="#fff" stroke-width="5" stroke-linecap="round" stroke-linejoin="round"/></svg>
    <div class="service" style="left:500px">
      <div class="icon"><svg width="64" height="64" viewBox="0 0 64 64"><text x="32" y="44" text-anchor="middle" font-family="Raleway, sans-serif" font-size="34" font-weight="700" fill="#4f6f8b">$</text></svg></div>
      <h3>Marketing</h3>
      <p>Lorem ipsum dolor sit amet, consectetur adipiscing elit, sed do eiusmod tempor incididunt ut labore.</p>
    </div>
    <svg class="arrow" style="left:712px" width="96" height="40" viewBox="0 0 96 40"><path d="M4 26 Q48 4 84 20" fill="none" stroke="#fff" stroke-width="5" stroke-linecap="round"/><path d="M72 8 L88 21 L70 30" fill="none" stroke="#fff" stroke-width="5" stroke-linecap="round" stroke-linejoin="round"/></svg>
    <div class="service" style="left:800px">
      <div class="icon"></div>
      <h3>Design</h3>
      <p>Lorem ipsum dolor sit amet, consectetur adipiscing elit, sed do eiusmod tempor incididunt ut labore.</p>
    </div>
  </section>

  <section class="reviews">
    <h2>What Customers are <strong>Saying</strong></h2>
    <div class="stars">
      <svg width="26" height="26" viewBox="0 0 24 24"><path d="M12 1l3.2 7 7.6.7-5.8 5 1.8 7.4L12 17.3 5.2 21.1 7 13.7 1.2 8.7l7.6-.7z" fill="#f47528"/></svg>
      <svg width="26" height="26" viewBox="0 0 24 24"><path d="M12 1l3.2 7 7.6.7-5.8 5 1.8 7.4L12 17.3 5.2 21.1 7 13.7 1.2 8.7l7.6-.7z" fill="#f47528"/></svg>
      <svg width="26" height="26" viewBox="0 0 24 24"><path d="M12 1l3.2 7 7.6.7-5.8 5 1.8 7.4L12 17.3 5.2 21.1 7 13.7 1.2 8.7l7.6-.7z" fill="#f47528"/></svg>
      <svg width="26" height="26" viewBox="0 0 24 24"><path d="M12 1l3.2 7 7.6.7-5.8 5 1.8 7.4L12 17.3 5.2 21.1 7 13.7 1.2 8.7l7.6-.7z" fill="#f47528"/></svg>
      <svg width="26" height="26" viewBox="0 0 24 24"><path d="M12 1l3.2 7 7.6.7-5.8 5 1.8 7.4L12 17.3 5.2 21.1 7 13.7 1.2 8.7l7.6-.7z" fill="#f47528"/></svg>
    </div>
    <div class="quote-mark">&ldquo;</div>
    <blockquote>Minim veniam, quis nostrud exercitation ullamco laboris nisi ut aliquip ex ea commodo consequat. Duis aute irure dolor in reprehenderit.</blockquote>
    <cite>Alan Morrow, Manager Inc</cite>
    <div class="dots"><span></span><span class="on"></span><span></span><span></span></div>
  </section>

  <div class="footer-brand"><span class="dot"></span>Copper Wayfarer</div>

  <footer class="footer">
    <div class="col about" style="left:188px">
      <h4>About <span>Us</span></h4>
      <p>Lorem ipsum dolor sit <em>amet</em> consectetur adipiscing elit sed do <em>eiusmod</em> tempor incididunt ut labore et dolore magna aliqua ut enim ad minim veniam</p>
    </div>
    <div class="col" style="left:440px">
      <h4>Quick <span>Links</span></h4>
      <ul>
        <li>Home</li>
        <li>About</li>
        <li>Service</li>
        <li>Portfolio</li>
        <li>Client reviews</li>
        <li>Contact</li>
      </ul>
    </div>
    <div class="col" style="left:648px">
      <h4>Social <span>Media</span></h4>
      <div class="socials">
        <span style="background:#3b5998" aria-label="Chatterly"></span>
        <span style="background:#dd4b39" aria-label="Plexo+"></span>
        <span style="background:#1da1f2" aria-label="Peepline"></span>
        <span style="background:#e52d27" aria-label="ReelHub"></span>
      </div>
    </div>
    <div class="bottom">
      <span class="copy">&copy; all rights reserved. Copyright</span>
      <span class="legal">Privacy | Policy</span>
    </div>
  </footer>

</div>
</body>
</html>
```